Dental office needs a newspaper ad to encourage new patients to join our practice

"October Teeth Whitening Special" Call today to schedule your next dental cleaning and exam and receive a free bleach kit. (small disclaimer at the bottom of the ad) Dr. Halvorsen and his staff follow the most up-to-date NHA infection control guidelines to protect our patients from CoVid-19 exposure. We offer a full spectrum of dental services including oral surgery, implants, root canals and cosmetic crowns and bridges. Our staff of licensed dental hygienists provide continued periodontal care for the healthiest teeth and gums. Visit our website. These are just some ideas you might be able to use. Also mention that most insurances are accepted. Emergencies and new patients welcome. As softer southern style motif like in our website can be used as a backdrop. The color scheme of the business logo and stationery is the same as the website.
Target Market(s)
All ages, local population 8,000 southern farming community. White Hispanic older population. Not oriented towards children.
Requirements
Must have
- Nice color. See our website at halvorsendentalcare.example for basic image of practice
Nice to have
- It will be a quarter to half page in a local newspaper, so it can be good sized with plenty of print an graphics

```html
<!DOCTYPE html>
<html lang="en">
<head>
<meta charset="utf-8">
<title>October Teeth Whitening Special – Halvorsen Dental</title>
<link href="https://fonts.googleapis.com/css2?family=Bebas+Neue&family=Open+Sans:wght@400;600;700&display=swap" rel="stylesheet">
<style>
  :root {
    --backdrop: #454746;
    --paper-top: #f4f8fd;
    --paper-bottom: #e6eff9;
    --green: #27b35a;
    --blue: #2f78d0;
    --navy: #1b4b8f;
    --name-blue: #1f5aa8;
    --ink: #1c1c1c;
    --white: #ffffff;
  }
  * { box-sizing: border-box; margin: 0; padding: 0; }
  html, body { width: 1200px; height: 1200px; overflow: hidden; }
  body { background: var(--backdrop); font-family: "Open Sans", Arial, sans-serif; }

  .ad {
    position: absolute; left: 80px; top: 211px; width: 1023px; height: 770px;
    background: linear-gradient(180deg, var(--paper-top), var(--paper-bottom));
    box-shadow: 0 10px 28px rgba(0,0,0,.35);
    overflow: hidden;
  }

  .headline { position: absolute; left: 32px; top: 46px; font-family: "Bebas Neue", Impact, sans-serif; font-weight: 400; font-size: 82px; line-height: 72px; white-space: nowrap; }
  .headline .line-green { color: var(--green); display: block; }
  .headline .line-blue { color: var(--blue); display: block; }
  .headline-rule { position: absolute; left: 32px; top: 190px; width: 110px; height: 8px; background: var(--green); }

  .safety-note { position: absolute; left: 32px; top: 220px; width: 480px; font-size: 17px; line-height: 24px; color: var(--ink); }
  .safety-note strong { font-weight: 700; }

  .services-band { position: absolute; left: 0; top: 315px; width: 495px; height: 46px; }
  .services-band svg { position: absolute; inset: 0; }
  .services-band h2 { position: relative; padding-left: 36px; font-family: "Bebas Neue", Impact, sans-serif; font-weight: 400; font-size: 39px; line-height: 48px; color: var(--white); white-space: nowrap; }

  .service-list { position: absolute; top: 381px; list-style: none; font-size: 23px; line-height: 26px; color: var(--ink); }
  .service-list li { position: relative; padding-left: 34px; margin-bottom: 14px; }
  .service-list li svg { position: absolute; left: 0; top: 6px; }
  .service-list.col-a { left: 36px; }
  .service-list.col-b { left: 244px; }
  .service-list.col-b li { padding-left: 36px; }

  .practice-mark { position: absolute; left: 88px; top: 560px; width: 38px; height: 38px; border-radius: 50%; background: var(--name-blue); }
  .practice-name { position: absolute; left: 152px; top: 556px; font-size: 30px; font-weight: 600; color: var(--name-blue); letter-spacing: -0.5px; white-space: nowrap; }
  .practice-address { position: absolute; left: 152px; top: 604px; font-size: 19px; color: var(--ink); display: flex; align-items: center; gap: 12px; white-space: nowrap; }

  .portrait { position: absolute; left: 616px; top: 29px; width: 407px; height: 455px;
    background: radial-gradient(ellipse at 55% 35%, #e9c1a8 0 22%, #6b3e2a 40%, #7a9cc4 72%, rgba(230,239,249,0) 90%); }

  .phone-band { position: absolute; left: 536px; top: 482px; width: 487px; height: 78px; }
  .phone-band svg.band { position: absolute; inset: 0; }
  .phone-number { position: absolute; left: 66px; top: 10px; display: flex; align-items: center; gap: 14px; font-family: "Bebas Neue", Impact, sans-serif; font-size: 56px; line-height: 60px; color: var(--white); white-space: nowrap; }

  .offer-box { position: absolute; left: 509px; top: 560px; width: 514px; height: 104px; }
  .offer-box svg { position: absolute; inset: 0; }
  .offer-box p { position: relative; padding: 10px 0 0 69px; font-size: 21px; line-height: 27px; color: var(--white); white-space: nowrap; }
  .offer-box strong { font-weight: 700; }

  .footer-bar { position: absolute; left: 0; top: 663px; width: 1023px; height: 107px; background: var(--green); color: var(--white); font-size: 26px; white-space: nowrap; }
  .footer-bar .welcome { position: absolute; left: 38px; top: 24px; }
  .footer-bar .insurance { position: absolute; left: 598px; top: 22px; }
  .footer-bar .divider { position: absolute; left: 567px; top: 8px; width: 2px; height: 90px; background: var(--white); }
</style>
</head>
<body>
  <main class="ad">
    <h1 class="headline">
      <span class="line-green">October Teeth</span>
      <span class="line-blue">Whitening Special</span>
    </h1>
    <div class="headline-rule"></div>

    <p class="safety-note">Dr. Halvorsen and his staff follow the most up-to-date NHA infection control guidelines to protect our patients from <strong>CoVid-19 exposure.</strong></p>

    <div class="services-band">
      <svg width="495" height="46" viewBox="0 0 495 46"><polygon points="0,0 487,0 495,46 0,46" fill="var(--green)"/></svg>
      <h2>All Phases of General Dentistry</h2>
    </div>

    <ul class="service-list col-a">
      <li><svg width="22" height="18" viewBox="0 0 22 18"><path d="M2 9 L8 15 L20 2" fill="none" stroke="var(--green)" stroke-width="4"/></svg>Oral Surgery</li>
      <li><svg width="22" height="18" viewBox="0 0 22 18"><path d="M2 9 L8 15 L20 2" fill="none" stroke="var(--green)" stroke-width="4"/></svg>Implants</li>
    </ul>
    <ul class="service-list col-b">
      <li><svg width="22" height="18" viewBox="0 0 22 18"><path d="M2 9 L8 15 L20 2" fill="none" stroke="var(--green)" stroke-width="4"/></svg>Root Canals</li>
      <li style="line-height:24px"><svg width="22" height="18" viewBox="0 0 22 18"><path d="M2 9 L8 15 L20 2" fill="none" stroke="var(--green)" stroke-width="4"/></svg>Cosmetic Crowns<br>&amp; Bridges</li>
    </ul>

    <div class="practice-mark"></div>
    <div class="practice-name">Martin E. Halvorsen, DMD</div>
    <div class="practice-address">
      <svg width="22" height="26" viewBox="0 0 22 26"><path d="M11 1 C5 1 1 5.5 1 11 C1 18 11 25 11 25 C11 25 21 18 21 11 C21 5.5 17 1 11 1 Z" fill="var(--green)"/><circle cx="11" cy="11" r="4" fill="var(--white)"/></svg>
      48 Magnolia Ave. in Fairbrook
    </div>

    <div class="portrait" role="img" aria-label="Portrait photo of a smiling woman with long curly brown hair in a denim shirt"></div>

    <div class="phone-band">
      <svg class="band" width="487" height="78" viewBox="0 0 487 78"><polygon points="16,0 487,0 487,78 0,78" fill="var(--blue)"/></svg>
      <div class="phone-number">
        <svg width="46" height="44" viewBox="0 0 46 44">
          <path d="M8 6 C4 8 2 12 4 18 C8 28 16 36 26 40 C32 42 36 40 38 36 L32 29 C30 30 28 31 26 30 C20 27 16 23 13 17 C12 15 13 13 14 12 Z" fill="var(--white)"/>
          <path d="M26 10 A10 10 0 0 1 34 18 M27 3 A17 17 0 0 1 41 17" fill="none" stroke="var(--white)" stroke-width="3" stroke-linecap="round"/>
        </svg>
        (555) 201 - 4836
      </div>
    </div>

    <div class="offer-box">
      <svg width="514" height="104" viewBox="0 0 514 104"><polygon points="27,0 514,0 514,104 0,104" fill="var(--navy)"/></svg>
      <p><strong>CALL TODAY</strong> to schedule your next<br>dental cleaning and exam and receive<br>a <strong>FREE BLEACH KIT.</strong></p>
    </div>

    <footer class="footer-bar">
      <span class="welcome">Emergencies and New Patients Welcome</span>
      <span class="divider"></span>
      <span class="insurance">Most Insurances are Accepted</span>
    </footer>
  </main>
</body>
</html>
```